The book title is:

The Quietly Capable Schedule Keeper

Ewan Holloway, MSc, MBA, PMP

It is a book about professional yet common sense project management principles aimed at beginner to experienced project managers. The book is written in a conversational, informal tone with reference to best practice in project management. It is designed to be used as an accessible desk reference. I am looking for a cover design that is striking, eye catching, and professional. It can have an element of fun and informality to reflect the tone of the contents.

I have attached a copy of the draft manuscript so you can get a feel for what the book is like.

see www.taskguildnet.org for more about the profession of project management

Target Market(s)

Professional Project Managers of all levels (see www.taskguildnet.org for further information)

Industry/Entity Type

Management

Requirements
Must have
• Must be suitable for 6" x 9" book size

```html
<!DOCTYPE html>
<html lang="en">
<head>
<meta charset="utf-8">
<title>The Quietly Capable Schedule Keeper — Cover</title>
<link rel="stylesheet" href="https://fonts.googleapis.com/css2?family=Stint+Ultra+Condensed&family=EB+Garamond:ital@1&family=Arimo:wght@700&display=swap">
<style>
  :root {
    --cover-blue: #0a77c2;
    --paper: #ffffff;
    --ink: #0d0d0d;
  }
  html, body {
    margin: 0;
    padding: 0;
    width: 901px;
    height: 1200px;
    overflow: hidden;
    background: var(--paper);
  }
  .cover {
    position: relative;
    width: 901px;
    height: 1200px;
    background: var(--paper);
    overflow: hidden;
  }
  .cover__blocks {
    position: absolute;
    inset: 0;
  }
  .cover__blocks path { fill: var(--cover-blue); }

  .tagline {
    position: absolute;
    left: 0;
    top: 84px;
    width: 690px;
    text-align: right;
    margin: 0;
    font-family: "EB Garamond", Georgia, serif;
    font-style: italic;
    font-size: 29px;
    letter-spacing: 2.4px;
    color: var(--ink);
  }

  .title {
    margin: 0;
    font-family: "Stint Ultra Condensed", "Arial Narrow", serif;
    font-weight: 400;
    color: var(--ink);
  }
  .title__line {
    position: absolute;
    background: var(--paper);
    line-height: 0.86;
    padding: 4px 10px 6px 6px;
    white-space: nowrap;
  }
  .title__line--the      { left: 86px;  top: 238px; font-size: 128px; }
  .title__line--quietly  { left: 226px; top: 338px; font-size: 128px; }
  .title__line--capable  { left: 226px; top: 455px; font-size: 128px; }
  .title__line--schedule { left: 259px; top: 566px; font-size: 218px; padding-right: 12px; }
  .title__line--keeper   { left: 431px; top: 775px; font-size: 128px; }

  .author {
    position: absolute;
    top: 1108px;
    left: 0;
    width: 901px;
    margin: 0;
    font-family: "Arimo", Arial, sans-serif;
    font-weight: 700;
  }
  .author__name {
    position: absolute;
    right: 398px;
    font-size: 25px;
    letter-spacing: -0.6px;
    color: var(--paper);
  }
  .author__credentials {
    position: absolute;
    left: 505px;
    font-size: 22px;
    top: 2px;
    letter-spacing: -0.3px;
    color: var(--ink);
  }
</style>
</head>
<body>
  <main class="cover">
    <svg class="cover__blocks" width="901" height="1200" viewBox="0 0 901 1200" aria-hidden="true">
      <path class="corner-step" d="M565 0 H759 V211 H707 V29 H565 Z"/>
      <path class="title-staircase" d="M0 238 H86 V333 H226 V566 H259 V758 H431 V888 H513 V1200 H0 Z"/>
    </svg>

    <p class="tagline">Make your own way to project success</p>

    <h1 class="title">
      <span class="title__line title__line--the">The</span>
      <span class="title__line title__line--quietly">Quietly</span>
      <span class="title__line title__line--capable">Capable</span>
      <span class="title__line title__line--schedule">Schedule</span>
      <span class="title__line title__line--keeper">Keeper</span>
    </h1>

    <p class="author">
      <span class="author__name">Ewan Holloway</span>
      <span class="author__credentials">, MSc, MBA, PMP</span>
    </p>
  </main>
</body>
</html>
```